KRV Business Cards

We are a local commercial development company based in Silicon Valley and we would like a new business card. I've attached a copy of our company brochure to give a flavor of what we do, our logo, info company colors/graphics, and our current business card. We don't necessarily need a crazy makeover, but would like something that feels a little bit more "fresh" and modern (we've had the same business card design for 15+ years), but still in keeping with our overall brand -- clean, high-quality, modern but timeless. Would like to add our website to the info on the card (www.velmara.com) and would like the flexibility for some folks to have an efax number listed and some not to have that included (without it looking like there is a hole).

```html
<!DOCTYPE html>
<html lang="en">
<head>
<meta charset="utf-8">
<title>KRV Business Cards</title>
<link rel="stylesheet" href="https://fonts.googleapis.com/css2?family=Cinzel:wght@400;500&family=Tinos:ital,wght@0,400;1,400;1,700&display=swap">
<style>
  :root {
    --slate: #435a72;
    --paper: #ffffff;
    --ink: #435a72;
    --text: #4a5563;
    --backdrop: #e9e8e5;
  }
  * { box-sizing: border-box; margin: 0; padding: 0; }
  html, body { width: 1200px; height: 1200px; overflow: hidden; }
  body { background: var(--backdrop); position: relative; font-family: "Tinos", "Times New Roman", serif; }

  .card { position: absolute; box-shadow: 0 2px 8px rgba(0,0,0,.12); }

  /* Front */
  .card-front { left: 219px; top: 130px; width: 751px; height: 431px; background: var(--paper); }
  .brand-block { position: absolute; left: 0; top: 28px; width: 413px; height: 209px; background: var(--slate); }
  .brand-name {
    position: absolute; left: 33px; top: 34px;
    font-family: "Cinzel", serif; font-weight: 400; color: var(--paper);
    font-size: 42px; line-height: 48px; letter-spacing: .5px;
  }
  .suffix { font-size: 31px; }
  .base-strip { position: absolute; left: 0; bottom: 0; width: 413px; height: 13px; background: var(--slate); }

  .person { position: absolute; left: 449px; top: 72px; color: var(--ink); }
  .person-name { font-family: "Cinzel", serif; font-weight: 500; font-size: 31px; line-height: 34px; letter-spacing: .3px; }
  .person-title { font-family: "Tinos", serif; font-style: italic; font-size: 21px; line-height: 20px; margin-left: 2px; }

  .contact { position: absolute; left: 445px; top: 246px; color: var(--text); font-size: 18.5px; line-height: 22px; }
  .contact-row { display: flex; margin-bottom: 7.5px; }
  .contact-row dt { width: 73px; font-style: italic; font-weight: 700; color: var(--ink); }
  .contact-row dd { color: var(--text); }

  /* Back */
  .card-back { left: 216px; top: 630px; width: 766px; height: 438px; background: var(--slate); }
  .back-name {
    position: absolute; left: 61px; top: 112px;
    font-family: "Cinzel", serif; font-weight: 400; color: var(--paper);
    font-size: 66px; line-height: 66px; letter-spacing: 1px;
  }
  .back-name .suffix { font-size: 48px; }
  .website {
    position: absolute; left: 0; right: 0; top: 404px; text-align: center;
    font-family: "Cinzel", serif; font-weight: 500; color: var(--paper);
    font-size: 15px; letter-spacing: .8px;
  }
</style>
</head>
<body>
  <section class="card card-front">
    <div class="brand-block">
      <h1 class="brand-name">KINROSS<br>RIVER<br>VENTURES, <span class="suffix">LLC</span></h1>
    </div>
    <div class="base-strip"></div>
    <div class="person">
      <p class="person-name">Elena J. Marsh</p>
      <p class="person-title">partner</p>
    </div>
    <dl class="contact">
      <div class="contact-row"><dt>address.</dt><dd>218 Linden Court,<br>Lindenvale, California 95012</dd></div>
      <div class="contact-row"><dt>email.</dt><dd>elena@velmara.com</dd></div>
      <div class="contact-row"><dt>direct.</dt><dd>650.555.0138</dd></div>
      <div class="contact-row"><dt>main.</dt><dd>650.555.0100</dd></div>
      <div class="contact-row"><dt>fax.</dt><dd>650.555.0192</dd></div>
    </dl>
  </section>

  <section class="card card-back">
    <h2 class="back-name">KINROSS<br>RIVER<br>VENTURES, <span class="suffix">LLC</span></h2>
    <p class="website">www.velmara.com</p>
  </section>
</body>
</html>
```